Velborne Systems needs a business card

The logo we have uploaded is going to be the image centered on the back.
The business card color is going to be black. Increase the contrast in the logo and lettering so the grey stands out from the black and is more readable. Keep the shadow effect if you can.
On the front, the only part of the logo that should be used is the Egyptian character. We would like the following information included: Name (first last), Title, Phone number, email and company name (Velborne Systems).
The images of colored sound waves we uploaded is a concept we would like implemented on the front as well but please do not use the exact image. It is for guideline purposes.
Get creative with the empty space. We are a technology company that deals with sound and lights. Please not too busy.
Thank you, we look forward to all your submissions.

```html
<!DOCTYPE html>
<html lang="en">
<head>
<meta charset="utf-8">
<title>Velborne Systems – Business Card</title>
<link rel="stylesheet" href="https://fonts.googleapis.com/css2?family=Open+Sans:wght@400;600&display=swap">
<style>
  :root {
    --page-bg: #e9e6e1;
    --card-black: #2b2b2d;
    --card-black-deep: #1f1f21;
    --brand-red: #e8323c;
    --brand-red-soft: #f0626a;
    --paper-white: #fbfbfb;
    --ink-dark: #2a2a2a;
    --ink-grey: #555555;
  }
  * { margin: 0; padding: 0; box-sizing: border-box; }
  html, body {
    width: 1200px; height: 892px; overflow: hidden;
    background: var(--page-bg);
    font-family: "Open Sans", Arial, sans-serif;
  }
  .canvas {
    width: 1200px; height: 892px;
    display: flex; flex-direction: column; align-items: center; justify-content: center;
    gap: 56px;
  }
  .card {
    position: relative;
    width: 580px; height: 331px;
    border-radius: 4px;
    overflow: hidden;
    box-shadow: 0 10px 28px rgba(0,0,0,.25);
  }
  .card svg { position: absolute; inset: 0; }

  /* Front */
  .card-front { background: var(--paper-white); }
  .front-brand {
    position: absolute; left: 44px; top: 44px;
    display: flex; align-items: center; gap: 12px;
  }
  .brand-square { width: 22px; height: 22px; background: var(--brand-red); }
  .brand-name {
    font-weight: 600; font-size: 22px; letter-spacing: 3px;
    color: var(--brand-red); text-transform: uppercase;
  }
  .contact {
    position: absolute; left: 270px; top: 168px; width: 290px;
  }
  .contact-name { font-size: 26px; font-weight: 600; color: var(--brand-red); line-height: 1.15; }
  .contact-title { font-size: 13px; color: var(--ink-grey); margin-top: 1px; margin-left: 14px; }
  .contact-lines { list-style: none; margin-top: 14px; font-size: 14px; color: var(--ink-dark); line-height: 1.4; }

  /* Back */
  .card-back {
    background: linear-gradient(160deg, var(--card-black) 0%, var(--card-black-deep) 100%);
    display: flex; align-items: center; justify-content: center;
  }
  .back-brand { display: flex; align-items: center; gap: 16px; }
  .back-brand .brand-square { width: 30px; height: 30px; }
  .back-brand .brand-name { font-size: 28px; letter-spacing: 4px; }
</style>
</head>
<body>
<main class="canvas">

  <section class="card card-front" aria-label="Business card front">
    <svg width="580" height="331" viewBox="0 0 580 331" aria-hidden="true">
      <path d="M0 0 H580 V10 C480 90 320 128 0 138 Z" fill="var(--card-black)"/>
      <path d="M580 10 C480 90 320 128 0 138 L0 148 C320 142 480 108 580 32 Z" fill="var(--brand-red-soft)"/>
      <path d="M580 32 C480 108 320 142 0 148 L0 153 C330 148 490 118 580 42 Z" fill="var(--brand-red)"/>
      <rect x="0" y="307" width="580" height="24" fill="var(--brand-red)"/>
    </svg>
    <div class="front-brand">
      <span class="brand-square"></span>
      <span class="brand-name">Velborne Systems</span>
    </div>
    <div class="contact">
      <p class="contact-name">Employee Name</p>
      <p class="contact-title">Managing Director</p>
      <ul class="contact-lines">
        <li>Phone : 041-7293 5860</li>
        <li>Web : www.velborne-systems.test</li>
        <li>Email : hello@velborne-systems.test</li>
      </ul>
    </div>
  </section>

  <section class="card card-back" aria-label="Business card back">
    <div class="back-brand">
      <span class="brand-square"></span>
      <span class="brand-name">Velborne Systems</span>
    </div>
  </section>

</main>
</body>
</html>
```